New River III Precinct 6x11 GOTV postcard

We require BOTH persuasive copy and high-impact layout for an oversized 6x11 political mailer. This might be one person, but it likely requires a specialized "creative team." of an experienced political strategist copywriter PLUS a graphic designer - so the words fit the exact layout block, and the visuals reinforce the psychological punch of the headline.

The goal is to remove all excuses a targeted audience of ~900 registered Democratic + ~1800 Unaffiliated voters in our precinct - have for not voting.

I need to be able to work by phone / online chat to iterate designs
I need to own the design in the top couple of software outputs that any printer service will require.

I want to experiment with very subtle background images as follows:
- Front of postcard that conveys "CHANGE" of not just seasons - but of encouraging change of precinct voter representation - so anything about fall foliage / conveyance of change tie-in is worthy of considering
- Back of postcard - any Appalachian long rage mountain view that includes 5-7 layers of hills in the distance.
Some photos as samples to consider.

Target Market(s)

~2,700 registered Democrats and Unaffiliated voters

Requirements
Must have
• We require BOTH persuasive copy and high-impact layout for an oversized 6x11 political mailer. This might be one person, but it likely requires a specialized "creative team." of an experienced political strategist copywriter PLUS a graphic designer - so the words fit the exact layout block, and the visuals reinforce the psychological punch of the headline
Nice to have
• subtle background photos

```html
<!DOCTYPE html>
<html lang="en">
<head>
<meta charset="utf-8">
<title>New River III Precinct Postcard</title>
<link href="https://fonts.googleapis.com/css2?family=Barlow:wght@400;500;600;700&family=Barlow+Condensed:wght@700&family=Roboto:wght@400&display=swap" rel="stylesheet">
<style>
:root{
  --stage:#c1c1c1;
  --paper:#ffffff;
  --navy:#262f85;
  --ballot-blue:#2b2f86;
  --red:#cc1535;
  --ink:#3a3a3a;
  --gold:#f1b53b;
  --gold-deep:#d98d2a;
  --stamp:#efefef;
  --banner-tint:#f2dde1;
}
*{box-sizing:border-box;margin:0;padding:0}
html,body{width:1090px;height:1200px;overflow:hidden;background:var(--stage)}
body{position:relative;font-family:"Barlow",sans-serif;color:var(--ink)}

.card{position:absolute;left:97px;width:897px;height:489px;background:var(--paper);overflow:hidden}
.card--front{top:93px}
.card--back{top:608px}

/* front: message side */
.flag-banner{position:absolute;left:0;top:0;width:561px;height:152px;background:linear-gradient(180deg,var(--banner-tint) 0%,rgba(242,221,225,.5) 60%,rgba(255,255,255,0) 100%)}
.headline{position:absolute;font-family:"Barlow Condensed",sans-serif;font-weight:700;line-height:1;white-space:nowrap}
.headline--top{left:191px;top:50px;font-size:63px;letter-spacing:-.6px;color:var(--navy)}
.headline--main{left:69px;top:103px;font-size:57px;letter-spacing:-.6px;color:var(--red)}

.issue{position:absolute}
.issue__title{display:flex;align-items:center;gap:5px;margin-left:-17px;font-weight:600;font-size:11px;color:var(--navy);line-height:1.1}
.issue__title svg{width:11px;height:11px;flex:none}
.issue__text{font-size:9px;line-height:11.6px;margin-top:1px}
.issue__text .cta{color:var(--red);font-weight:700;text-decoration:underline}
.col-a{left:52px;width:243px}
.col-b{left:330px;width:214px}

/* front: ballot side */
.ballot{position:absolute;left:561px;top:0;width:336px;height:489px}
.foliage{position:absolute;inset:0;background:radial-gradient(circle at 30% 20%,#f6cd5c,transparent 60%),linear-gradient(135deg,var(--gold),var(--gold-deep) 50%,var(--gold))}
.ballot__panel{position:absolute;left:16px;top:18px;width:306px;height:452px;background:var(--ballot-blue)}
.ballot__frame{position:absolute;left:31px;top:34px;width:274px;height:419px;border:1.5px dotted #f1c94a}
.ballot__heading{position:absolute;left:61px;font-weight:700;font-size:15px;line-height:16.5px;color:#fff}
.ballot__rule{position:absolute;left:61px;top:174px;width:220px;height:1px;background:#3d44a0}
.pick{position:absolute;left:65px;display:flex;gap:6px;color:#fff}
.pick svg{width:10px;height:10px;margin-top:1px;flex:none}
.pick__office{font-size:9.7px;line-height:12.2px}
.pick__name{font-size:9.7px;line-height:12.2px;font-weight:700}

/* back: address side */
.mountain-view{position:absolute;left:0;top:190px;width:897px;height:299px;background:linear-gradient(180deg,rgba(255,255,255,0) 0%,#e4e4e4 30%,#cfcfcf 55%,#8a8a8a 82%,#4c4c4c 100%)}
.letter{position:absolute;left:40px;top:42px;width:465px}
.letter__greeting{font-weight:700;font-size:16px;color:var(--navy);margin-bottom:7px;letter-spacing:-.3px}
.letter p{font-size:11px;line-height:13.7px;margin-bottom:5.5px;color:#333}
.voter-facts{position:absolute;left:41px;top:263px;font-size:11px;line-height:13.7px;color:var(--red)}
.postage{position:absolute;left:759px;top:21px;width:118px;height:101px;background:var(--stamp);font-family:"Roboto",sans-serif;font-size:11.5px;line-height:13.8px;text-align:center;color:#222;display:flex;align-items:center;justify-content:center}
.addressee{position:absolute;left:591px;top:159px;width:286px;height:101px;background:var(--stamp);display:flex;align-items:center;justify-content:center;text-align:center;font-size:15.5px;line-height:19.5px;color:#555}
</style>
</head>
<body>

<svg width="0" height="0" style="position:absolute">
  <defs>
    <symbol id="tick" viewBox="0 0 10 10">
      <circle cx="5" cy="5.4" r="3.8" fill="none" stroke="currentColor" stroke-width="1.2"/>
      <path d="M3 5.3 4.7 7 9.2 1.8" fill="none" stroke="#cc1535" stroke-width="1.5"/>
    </symbol>
  </defs>
</svg>

<section class="card card--front">
  <div class="flag-banner" role="img" aria-label="Waving American flag across the top of the card"></div>

  <div class="headline headline--top">VOTE FOR</div>
  <div class="headline headline--main">NEW REPRESENTATION</div>

  <div class="issue col-a" style="top:176px">
    <div class="issue__title"><svg><use href="#tick"/></svg>LOCAL PAIN—</div>
    <p class="issue__text">THANKS TO CURRENT REPRESENTATIVES — and sadly, to avoid accountability, they've cleverly delayed many / most impacts until AFTER the 2026 election. <span class="cta">VOTE FOR CHANGE</span></p>
  </div>
  <div class="issue col-a" style="top:230px">
    <div class="issue__title"><svg><use href="#tick"/></svg>FAMILY BUDGET—</div>
    <p class="issue__text">exploded costs for everything: groceries, gas, car insurance, rent.</p>
  </div>
  <div class="issue col-a" style="top:272px">
    <div class="issue__title"><svg><use href="#tick"/></svg>HEALTH—</div>
    <p class="issue__text">expired subsidies, tax credits mean ~1m in NC will lose coverage or pay more. 50% cuts to Hospitals, Mental Health facilities, rural facilities will be closing.</p>
  </div>
  <div class="issue col-a" style="top:326px">
    <div class="issue__title"><svg><use href="#tick"/></svg>REPRODUCTIVE RIGHTS—</div>
    <p class="issue__text">Government authoritarian intrusion - censure women's rights.</p>
  </div>
  <div class="issue col-a" style="top:368px">
    <div class="issue__title"><svg><use href="#tick"/></svg>FOOD SECURITY—</div>
    <p class="issue__text">Weaponized Hunger - cuts to SNAP; school meals cut; add'l work reqmts.</p>
  </div>
  <div class="issue col-a" style="top:411px">
    <div class="issue__title"><svg><use href="#tick"/></svg>EDUCATION—</div>
    <p class="issue__text">Watauga $2.2mm shortfall personnel cuts, freezes in hiring, teacher training. Abandoning civil rights of Special Ed students to HHS and DOL.</p>
  </div>

  <div class="issue col-b" style="top:176px">
    <div class="issue__title"><svg><use href="#tick"/></svg>HOUSING—</div>
    <p class="issue__text">~25% of renters are spending over 50% of income on rent. Especially bad locally; predatory leasing terms and skyrocketing rents. Proposed legislation is transforming HUD with the goal of getting rid of Section 8 housing that cares for vulnerable populations.</p>
  </div>
  <div class="issue col-b" style="top:265px">
    <div class="issue__title"><svg><use href="#tick"/></svg>ENERGY—</div>
    <p class="issue__text">In 2022 Boone achieved 100% renewable energy in town buildings; this is now being destroyed by repeal of renewable energy project funding. Ridgeline State Innovation District prepares renewable workforce technologies-all this is now in limbo.</p>
  </div>
  <div class="issue col-b" style="top:342px">
    <div class="issue__title"><svg><use href="#tick"/></svg>ENVIRONMENT—</div>
    <p class="issue__text">Reduced protections from coal ash pond leaks threaten public health. Corporations not held responsible for damage; public picks up the tab. Environmental justice enforcement no longer a priority. Logging in Watauga with no public oversight. It's the "haz-mat" model do nothing, wait for catastrophe, then fix it.</p>
  </div>

  <aside class="ballot">
    <div class="foliage" role="img" aria-label="Border of golden fall leaves"></div>
    <div class="ballot__panel"></div>
    <div class="ballot__frame"></div>

    <h2 class="ballot__heading" style="top:54px">SAMPLE BALLOT<br>RECOMMENDATIONS</h2>
    <div class="pick" style="top:96px"><svg><use href="#tick" color="#fff"/></svg><div><div class="pick__office">US SENATE –</div><div class="pick__name">DALE WHITMORE</div></div></div>
    <div class="pick" style="top:135px"><svg><use href="#tick" color="#fff"/></svg><div><div class="pick__office">US HOUSE – DISTRICT 5 –</div><div class="pick__name">RAY ASHFORD</div></div></div>

    <div class="ballot__rule"></div>

    <h2 class="ballot__heading" style="top:188px">REQMT TO SHOW ID FOR VOTERS<br>NOT IN PERSON – NO</h2>
    <div class="pick" style="top:232px"><svg><use href="#tick" color="#fff"/></svg><div><div class="pick__office">STATE SENATE DISTRICT 47 –</div><div class="pick__name">DALE WHITMORE</div></div></div>
    <div class="pick" style="top:269px"><svg><use href="#tick" color="#fff"/></svg><div><div class="pick__office">HOUSE OF REP'S DISTRICT 93 –</div><div class="pick__name">GLEN HARLOW</div></div></div>
    <div class="pick" style="top:306px"><svg><use href="#tick" color="#fff"/></svg><div><div class="pick__office">NC SUPREME COURT –</div><div class="pick__name">MARIAN OAKES</div></div></div>
    <div class="pick" style="top:343px"><svg><use href="#tick" color="#fff"/></svg><div><div class="pick__office">NC COURT OF APPEALS – SEAT 1 –</div><div class="pick__name">NEIL BRANTLEY</div></div></div>
    <div class="pick" style="top:380px"><svg><use href="#tick" color="#fff"/></svg><div><div class="pick__office">NC COURT OF APPEALS – SEAT 2 –</div><div class="pick__name">WES COLFAX</div></div></div>
    <div class="pick" style="top:416px"><svg><use href="#tick" color="#fff"/></svg><div><div class="pick__office">NC COURT OF APPEALS – SEAT 3 –</div><div class="pick__name">IRENE KOWAL</div></div></div>
  </aside>
</section>

<section class="card card--back">
  <div class="mountain-view" role="img" aria-label="Soft black and white view of layered Appalachian mountain ridges with trees in the foreground"></div>

  <div class="letter">
    <h1 class="letter__greeting">Dear New River III Neighbor.</h1>
    <p>We live in a representative democracy. We expect our representatives will exercise independent thinking and support policies and legislation that don't harm us - and that reflect the MAJORITY VIEWS of precinct citizens.</p>
    <p>But our current representatives HAVE STOPPED LISTENING - they are now bringing harmful policies straight to Watauga County. IT'S TIME TO HOLD THEM ACCOUNTABLE AND VOTE THEM OUT.</p>
    <p>Make no mistake: in 2026, every election is partisan. Even Judicial seats are now tied directly to state platforms.</p>
    <p>Any candidate who refuses to publicly condemn Raleigh's gerrymandered overreach into Watauga politics-or refuses to fight funding cuts for our healthcare, education, and environmental justice - is actively supporting these harmful policies.</p>
    <p>They are hoping their silence fools you. DON'T BE FOOLED. This November, VOTE FOR CHANGE.</p>
  </div>

  <div class="voter-facts">
    YOU ARE A REGISTERED VOTER IN WATAUGA COUNTY<br>
    YOU RESIDE IN PRECINCT: NEW RIVER III<br>
    POLLING PLACES AVAILABLE TO YOU ARE: LOCATION,. 2, 3<br>
    EARLY VOTING STARTS ON:<br>
    DEADLINE TO APPLY FOR MAIL-IN BALLOTS<br>
    KNOW THE RULES TO ENSURE YOUR MAIL-IN-BALLOT COUNTS
  </div>

  <div class="postage">Presorted<br>First-Class Mail<br>U.S. Postage Paid<br>59047<br>MailPressDirect.com</div>
  <div class="addressee">Local Postal<br>Customer</div>
</section>

</body>
</html>
```